Report template for evaluation reports to be used by non designers

We are looking for a report template that meets all the requirements listed in the attached documents. letter head, logo etc have been enclosed. Its important that the colour integrity is kept, but beyond that options are welcome.
Its important that the document is extremely easy to use and that is able to be adapted to include eatables, figures, pictures, text boxes etc and keep the integrity of the template

Target Market(s)

Governments, Civil society organisations and research institutions

Font styles to use
Sans Serif

Colors
6b449b
876aae
c0c0c0
000000

Requirements
Must have
• Clean, professional, not concluded, modern, must be easy to use
Should not have
• too busy, hard to use

```html
<!DOCTYPE html>
<html lang="en">
<head>
<meta charset="utf-8">
<title>Civitas Report Template – Page Overview</title>
<link rel="stylesheet" href="https://fonts.googleapis.com/css2?family=Open+Sans:wght@300;400;600;700&display=swap">
<style>
  :root{
    --purple:#6b449b;
    --lilac:#876aae;
    --silver:#c0c0c0;
    --black:#000000;
    --ink:#3a3a3a;
    --muted:#6f6f6f;
    --stage:#d4d4d6;
    --tint:#e6def0;
    --photo-a:#8d8f96;
    --photo-b:#d9d6d2;
  }
  *{box-sizing:border-box;margin:0;padding:0}
  html,body{width:1200px;height:1200px;overflow:hidden}
  body{background:var(--stage);font-family:"Open Sans",Arial,sans-serif;color:var(--ink);position:relative}
  .page{position:absolute;width:268px;height:347px;background:#fff;box-shadow:0 2px 5px rgba(0,0,0,.28);overflow:hidden}
  .c1{left:35px}.c2{left:319px}.c3{left:613px}.c4{left:902px}
  .r1{top:43px}.r2{top:408px}.r3{top:774px}

  .logo{position:absolute;display:flex;align-items:center;gap:4px;font-weight:600;letter-spacing:.16em;color:#222}
  .logo .dot{border-radius:50%;background:var(--purple)}
  .logo.lg{font-size:20px}.logo.lg .dot{width:9px;height:9px}
  .logo.light{color:#fff}
  .logo.sm{font-size:7px;letter-spacing:.14em}.logo.sm .dot{width:3px;height:3px}

  .para{font-size:4.1px;line-height:6.2px;color:var(--ink)}
  .para p{margin-bottom:5px}
  .lead{color:var(--purple);font-weight:600}
  .sub{font-size:6.6px;color:var(--muted);font-weight:400;margin:8px 0 3px}
  .mini{font-size:4.4px;color:var(--purple);margin:6px 0 2px}

  .pgtitle{position:absolute;left:24px;right:24px;top:22px;text-align:center;font-size:10px;color:#222;letter-spacing:.01em;padding-bottom:5px;border-bottom:.6px solid var(--silver)}
  .pgtitle b{font-weight:400;color:var(--purple)}
  .body{position:absolute;left:24px;right:24px;top:44px}

  .foot{position:absolute;left:0;right:0;bottom:8px;height:6px}
  .foot .url{position:absolute;left:0;width:58%;height:4px;top:1px;background:var(--purple);font-size:3.4px;color:#fff;line-height:4px;padding-left:24px;clip-path:polygon(0 0,100% 0,97% 100%,0 100%)}
  .foot .logo{left:64%;top:-1px}
  .foot .num{position:absolute;right:0;width:13%;height:4px;top:1px;background:var(--black);color:#fff;font-size:3.4px;line-height:4px;padding-left:10px;clip-path:polygon(6% 0,100% 0,100% 100%,0 100%)}

  ul.sq{list-style:none}
  ul.sq li{position:relative;padding-left:5px;margin-bottom:1px}
  ul.sq li::before{content:"";position:absolute;left:0;top:2px;width:2.2px;height:2.2px;background:var(--purple)}
  ul.arrow{list-style:none;margin-left:28px}
  ul.arrow li{position:relative;padding-left:5px;margin-bottom:1px}
  ul.arrow li::before{content:"";position:absolute;left:0;top:1.6px;border-left:3px solid #222;border-top:1.5px solid transparent;border-bottom:1.5px solid transparent}

  table{border-collapse:separate;border-spacing:1px;width:100%;font-size:3.6px}
  th{background:var(--purple);color:#fff;font-weight:400;height:6px}
  td{background:#f0ecf5;height:6px;padding-left:5px}
  td.n{text-align:center;padding:0}
  tr.ph td{background:var(--tint);color:var(--purple);font-weight:600}
  tr.tot td{background:var(--lilac);color:#fff;font-weight:600}
  tr.grand td{background:var(--purple);color:#fff;font-weight:600}

  .photo{position:absolute;background:linear-gradient(135deg,var(--photo-a),var(--photo-b))}
</style>
</head>
<body>

<!-- Cover A -->
<section class="page c1 r1">
  <div class="photo" role="img" aria-label="Geometric cover artwork in purple, black and slate blue" style="left:0;top:0;width:92px;height:347px;background:linear-gradient(180deg,#1a1a1a 0%,var(--purple) 20%,#8ea0c2 38%,var(--purple) 55%,#111 68%,#9aaccd 85%,#fff 100%)"></div>
  <div class="logo lg" style="left:142px;top:30px"><span>CIVITAS</span><span class="dot"></span></div>
  <h1 style="position:absolute;left:113px;top:100px;font-size:12.5px;font-weight:700;color:#111">PROPOSAL TEMPLATE</h1>
  <div style="position:absolute;right:24px;top:233px;font-size:5px;color:var(--purple)">Proposal Presented to</div>
  <div style="position:absolute;right:24px;top:246px;font-size:11px;font-weight:700;color:#111">XYZ COMPANY</div>
  <div style="position:absolute;right:24px;top:320px;font-size:9px;color:#333">22 June 2018</div>
</section>

<!-- Cover B -->
<section class="page c2 r1" style="background:#7b7b7d">
  <div class="logo lg light" style="left:76px;top:24px"><span>CIVITAS</span><span class="dot"></span></div>
  <div class="photo" role="img" aria-label="Photograph of hands writing notes at a meeting table" style="left:0;top:78px;width:268px;height:182px;background:linear-gradient(160deg,#3b3b3d,#a9a7a4 55%,#ece9e4)"></div>
  <div style="position:absolute;left:0;right:0;top:264px;height:1.5px;background:#fff"></div>
  <div style="position:absolute;left:0;right:0;top:274px;text-align:center;color:#fff">
    <div style="font-size:11.5px;font-weight:700">PROPOSAL TEMPLATE</div>
    <div style="font-size:5.2px;margin-top:3px">Proposal Presented to</div>
    <div style="font-size:11px;font-weight:700;margin-top:5px">XYZ COMPANY</div>
    <div style="font-size:6.2px;margin-top:7px">22 June 2018</div>
  </div>
</section>

<!-- Version page -->
<section class="page c3 r1">
  <table style="position:absolute;left:42px;top:36px;width:186px;font-size:3.4px;border-spacing:0;border:.5px solid var(--lilac)">
    <tr><td style="background:#fff;border:.4px solid var(--lilac)">Version #</td><td style="background:#fff;border:.4px solid var(--lilac)">Purpose / Changes</td><td style="background:#fff;border:.4px solid var(--lilac)">Author</td><td style="background:#fff;border:.4px solid var(--lilac)">Date</td></tr>
    <tr><td style="background:var(--tint)"></td><td style="background:var(--tint)"></td><td style="background:var(--tint)"></td><td style="background:var(--tint)"></td></tr>
    <tr><td style="background:#fff"></td><td style="background:#fff"></td><td style="background:#fff"></td><td style="background:#fff"></td></tr>
    <tr><td style="background:var(--tint)"></td><td style="background:var(--tint)"></td><td style="background:var(--tint)"></td><td style="background:var(--tint)"></td></tr>
    <tr><td style="background:#fff"></td><td style="background:#fff"></td><td style="background:#fff"></td><td style="background:#fff"></td></tr>
    <tr><td style="background:var(--tint)"></td><td style="background:var(--tint)"></td><td style="background:var(--tint)"></td><td style="background:var(--tint)"></td></tr>
    <tr><td style="background:#fff"></td><td style="background:#fff"></td><td style="background:#fff"></td><td style="background:#fff"></td></tr>
  </table>
  <div class="para" style="position:absolute;left:53px;top:282px;width:176px;font-size:3.5px;line-height:5px">
    <div style="color:var(--purple)">Copyright xxxxx xxxxLimited<br>All Rights Reserved</div>
    <div style="border-top:.5px solid var(--silver);margin-top:4px;padding-top:3px">No part of the contents of this document may be reproduced or distributed in any form or by any means without the prior written permission of xxxxxx Limited</div>
  </div>
</section>

<!-- Table of contents -->
<section class="page c4 r1">
  <div style="position:absolute;left:24px;right:24px;top:20px;text-align:center;font-size:9.5px;padding-bottom:4px;border-bottom:.6px solid var(--silver)"><span style="color:var(--purple)">TABLE OF</span> CONTENTS</div>
  <div style="position:absolute;left:24px;top:50px;font-size:8px;color:var(--muted)">Contents</div>
  <div class="para" style="position:absolute;left:24px;right:33px;top:64px;font-size:3.8px;line-height:8.6px">
    <div style="display:flex"><span>Table of Contents</span><span style="flex:1;border-bottom:.5px dotted #777;margin:0 3px 2.5px"></span><span>01</span></div>
    <div style="display:flex"><span>Executive Summary</span><span style="flex:1;border-bottom:.5px dotted #777;margin:0 3px 2.5px"></span><span>02</span></div>
    <div style="display:flex"><span>Our Understanding of Your Needs</span><span style="flex:1;border-bottom:.5px dotted #777;margin:0 3px 2.5px"></span><span>02</span></div>
    <div style="display:flex"><span>Our Recommendations</span><span style="flex:1;border-bottom:.5px dotted #777;margin:0 3px 2.5px"></span><span>03</span></div>
    <div style="display:flex"><span>Our Approach</span><span style="flex:1;border-bottom:.5px dotted #777;margin:0 3px 2.5px"></span><span>05</span></div>
    <div style="display:flex"><span>Budget and Timeframe</span><span style="flex:1;border-bottom:.5px dotted #777;margin:0 3px 2.5px"></span><span>07</span></div>
    <div style="display:flex"><span>Appendix A: About Harlow Bay</span><span style="flex:1;border-bottom:.5px dotted #777;margin:0 3px 2.5px"></span><span>10</span></div>
    <div style="display:flex"><span>Appendix B: Selected Client List</span><span style="flex:1;border-bottom:.5px dotted #777;margin:0 3px 2.5px"></span><span>10</span></div>
    <div style="display:flex"><span>Appendix C: Our Capabilities</span><span style="flex:1;border-bottom:.5px dotted #777;margin:0 3px 2.5px"></span><span>11</span></div>
    <div style="display:flex"><span>Appendix D: Our Process</span><span style="flex:1;border-bottom:.5px dotted #777;margin:0 3px 2.5px"></span><span>12</span></div>
  </div>
  <footer class="foot"><div class="url">www.website.com</div><div class="logo sm"><span>CIVITAS</span><span class="dot"></span></div><div class="num">01</div></footer>
</section>

<!-- Executive summary -->
<section class="page c1 r2">
  <h2 class="pgtitle"><b>EXECUTIVE</b> SUMMARY</h2>
  <div class="body para">
    <p>We are pleased to present this proposal for system implementation and website integration support. Since the organisation was founded we have worked at the forefront of implementing and integrating platforms with open source websites, email service providers and other applications that support the outreach, research and programme work of public organisations.</p>
    <div class="sub">What We’re Proposing</div>
    <p>We propose a phased implementation approach that moves the programme forward in steps, supporting the planned launch currently scheduled for March.</p>
    <div class="sub">What’s in our Proposal</div>
    <p>Within this proposal we address the specific requirements and how they translate into a hosted solution built on proven tools. We provide more information on the features, benefits and architecture of the platform, and we show the value of an approach developed by industry experts and adopted by leading organisations.</p>
    <p>If you have any questions or comments, please feel free to contact us directly.</p>
    <p>Sincerely,</p>
    <p style="margin-top:8px">xxxxxxxx<br>Partner and Co-Founder<br><span style="color:var(--purple)">xxxxxxxxxxxxxxxxxx</span><br>(xxx) xxx-xxxx</p>
  </div>
  <footer class="foot"><div class="url">www.website.com</div><div class="logo sm"><span>CIVITAS</span><span class="dot"></span></div><div class="num">01</div></footer>
</section>

<!-- Understanding -->
<section class="page c2 r2">
  <h2 class="pgtitle"><b>OUR UNDERSTANDING</b> OF YOUR NEEDS</h2>
  <div class="body para">
    <p>In the last two weeks of January we held several conversations with your staff and your technology partner. As a result of those conversations we have been able to gather the following high level goals for your project:</p>
    <div class="sub" style="margin-top:2px;line-height:7px">Cloudwise must be in place to support Kindred at launch and as the program evolves</div>
    <p class="lead">The most critical aspect of this implementation, both in terms of time sensitivity and functionality, is centred around support for the Kindred project. Our current understanding is as follows:</p>
    <ul class="sq">
      <li>Kindred will be comprised of a series of websites focused on organising institutions and individuals within specific community sectors, with the goal of increased public support and reduced risk from a changing climate.</li>
      <li>The primary goals of the application are:</li>
    </ul>
    <ul class="arrow">
      <li>capture information of individuals and organisations along with their roles</li>
      <li>track their progress on site specific lists and site interactions</li>
      <li>allow staff to push next steps to members in an automated style</li>
      <li>join online and offline outreach programmes with useful segmentation</li>
      <li>natively integrate with the family of sites and the email provider of choice</li>
    </ul>
    <ul class="sq" style="margin-top:4px">
      <li>The data architecture must be well defined but flexible to support the core needs of the sites as launch as well as anticipated needs in the future.</li>
    </ul>
    <ul class="arrow">
      <li>For instance, a faith based site may collect a denomination field, while other sites may not collect that field.</li>
      <li>Future interactions outside of the list may become necessary to track, and the team will need a systemic way to capture those interactions and segment them.</li>
    </ul>
    <ul class="sq" style="margin-top:4px">
      <li>The information collected from the sites must be combined with current information held within the organisation to provide a holistic view of institutions and individuals.</li>
    </ul>
  </div>
  <footer class="foot"><div class="url">www.website.com</div><div class="logo sm"><span>CIVITAS</span><span class="dot"></span></div><div class="num">01</div></footer>
</section>

<!-- Approach text -->
<section class="page c3 r2">
  <h2 class="pgtitle"><b>OUR</b> APPROACH</h2>
  <div class="body para">
    <div class="sub" style="margin-top:2px">Solution</div>
    <div class="mini">AI automated accounting</div>
    <p>Ledgerly builds automation in stages on top of its current system to reach full automation. It automates every manual task performed by the user, starting by connecting to all sources of accounting data such as bank accounts, credit cards, webshops and document management systems. Based on these data it creates bookings and generates financial reports, and features a chat-like interface that lets users communicate seamlessly with it over time.</p>
    <div class="mini">Blockchain software license or Token-as-a-License</div>
    <p>It is possible to create tokens on a blockchain that represent software licenses. Ledgerly creates these tokens using the Basalt official wallet, and holders are free to transfer or sell them using a secondary market built directly on the chain. The system checks the validity of a token against the chain, ensuring that holders have access to the software and making resale easier for owners.</p>
    <div class="sub">Pre-ICO Token sale</div>
    <p>To realise this innovative vision, Ledgerly is launching a pre-sale of tokens on the chain. A fixed number of tokens are available for purchase during a limited period. Each token represents a lifelong software license, and holders can use it for invoicing or accounting, or buy future monthly subscriptions.</p>
    <div class="sub">Future plans</div>
    <p>A future sale is planned between 18 and 24 months after the pre-sale. This offering will support the development of a fully decentralised, privacy-focused ecosystem of applications.</p>
  </div>
  <footer class="foot"><div class="url">www.website.com</div><div class="logo sm"><span>CIVITAS</span><span class="dot"></span></div><div class="num">01</div></footer>
</section>

<!-- Budget -->
<section class="page c4 r2">
  <h2 class="pgtitle"><b>BUDGET AND</b> TIMEFRAME</h2>
  <div class="body para">
    <div class="sub" style="margin-top:2px">Implementation Estimate</div>
    <p>The bulk of the implementation costs will be defined by discovery. Based on similar projects we expect the work to fall between 200 and 300 hours. The wide swing in phase one reflects the undefined nature of both the integration needs and our role in it; our focus in discovery will be to narrow down those requirements.</p>
    <table>
      <tr><th style="width:56%">Task</th><th>Hours</th><th>Cost</th></tr>
      <tr><td>Discovery</td><td class="n">40</td><td class="n">$8,000</td></tr>
      <tr class="ph"><td>Phase 1</td><td></td><td></td></tr>
      <tr><td>Discovery</td><td class="n">20-40</td><td class="n">$8,000</td></tr>
      <tr><td>Discovery</td><td class="n">20-40</td><td class="n">$8,000</td></tr>
      <tr><td>Discovery</td><td class="n">20-40</td><td class="n">$8,000</td></tr>
      <tr class="tot"><td>Total Phase 1</td><td class="n">80-240</td><td class="n">$16,800-40,000</td></tr>
      <tr class="ph"><td>Phase 2</td><td></td><td></td></tr>
      <tr><td>Discovery</td><td class="n">20-40</td><td class="n">$8,000</td></tr>
      <tr class="tot"><td>Total Phase 2</td><td class="n">80-240</td><td class="n">$16,800-40,000</td></tr>
      <tr class="grand"><td>Total Estimated Implementation Cost</td><td class="n">220-480</td><td class="n">$44,000-96,000</td></tr>
    </table>
    <div class="sub">Project Timeline</div>
    <p>Based on the information we have, the March launch date does not seem a realistic goal for all the work needed. We feel it is prudent to proceed with discovery before committing to that date, and we estimate the first phase will take between 7 and 12 weeks.</p>
    <table>
      <tr><th style="width:62%">Task</th><th>Weeks to Complete</th></tr>
      <tr><td>Discovery</td><td class="n">1-2</td></tr>
      <tr><td>Phase 1</td><td class="n">6-10</td></tr>
      <tr><td>Phase 2</td><td class="n">8-12</td></tr>
      <tr class="tot"><td>Total Number of Weeks</td><td></td></tr>
    </table>
  </div>
  <footer class="foot"><div class="url">www.website.com</div><div class="logo sm"><span>CIVITAS</span><span class="dot"></span></div><div class="num">01</div></footer>
</section>

<!-- Appendix C -->
<section class="page c1 r3">
  <h2 class="pgtitle"><b>APPENDIX C : OUR</b> CAPABILITIES</h2>
  <div class="body para">
    <p>At Harlow Bay we have lived and breathed every stage of the public sector lifecycle: from technology strategy to organisational development, from mission-driven work to supporter engagement, and from online to offline communication. Our primary charge is the effective selection and implementation of technologies, with a big-picture perspective on organisational success.</p>
    <p>Our clients engage us to help them with a diverse array of strategic and technical work. We regularly support organisations with:</p>
  </div>
  <div style="position:absolute;left:152px;top:112px;width:1px;height:160px;background:var(--purple)"></div>
  <div class="para" style="position:absolute;left:24px;width:118px;top:112px">
    <div class="sub" style="margin-top:0">Technology Assessment &amp; Strategy</div>
    <p>Because of our commitment to open tools, organisations often ask us to help recommend a comprehensive set of solutions. We bring our industry knowledge to bear in assessing your model, staffing, legacy toolset and objectives, and then recommend a combination of solutions tailored to your needs.</p>
    <div class="sub">Fieldstone Implementation</div>
    <p>While Fieldstone is a truly open-source solution, many organisations choose it as their online platform and work with us as their implementation partner. We get each organisation up and running with advanced supporter engagement forms and integration, tailoring each step around priorities for outreach, analytics and measurement.</p>
  </div>
  <div class="para" style="position:absolute;left:160px;width:90px;top:112px">
    <div class="sub" style="margin-top:0;color:var(--purple)">Services Include:</div>
    <ul class="sq" style="font-weight:600">
      <li>Stakeholder interviews</li><li>Organisational resource analysis</li><li>Current toolset assessment</li><li>Technology recommendations</li><li>Actionable rollout plan</li><li>Staffing &amp; process strategy</li>
    </ul>
    <div class="sub" style="margin-top:42px;color:var(--purple)">Services Include:</div>
    <ul class="sq" style="font-weight:600">
      <li>Technical solution design</li><li>Donation form buildout</li><li>Engagement form buildout</li><li>System integration</li><li>Custom dashboard development</li><li>Phased plan for growth</li>
    </ul>
  </div>
  <footer class="foot"><div class="url">www.website.com</div><div class="logo sm"><span>CIVITAS</span><span class="dot"></span></div><div class="num">01</div></footer>
</section>

<!-- Approach with photo -->
<section class="page c2 r3">
  <h2 class="pgtitle"><b>OUR</b> APPROACH</h2>
  <div class="photo" role="img" aria-label="Photograph of a team meeting around a conference table" style="left:24px;top:41px;width:220px;height:150px;background:linear-gradient(135deg,#6d7c8e,#c9c1b3 55%,#efece6)"></div>
  <div class="para" style="position:absolute;left:24px;right:24px;top:196px">
    <div class="sub" style="margin-top:0">Solution</div>
    <div class="mini">AI automated accounting</div>
    <p>Ledgerly builds automation in stages on top of its current system to reach full automation. It starts by connecting to all sources of accounting data such as bank accounts, credit cards, webshops and document systems. Based on these data it creates bookings and generates financial reports, acting as a trusted advisor over time.</p>
    <div class="mini">Blockchain software license or Token-as-a-License</div>
    <p>It is possible to create tokens on a blockchain that represent software licenses. Holders are free to transfer or sell them using a secondary market built directly on the chain.</p>
  </div>
  <footer class="foot"><div class="url">www.website.com</div><div class="logo sm"><span>CIVITAS</span><span class="dot"></span></div><div class="num">01</div></footer>
</section>

<!-- Approach with chart -->
<section class="page c3 r3">
  <h2 class="pgtitle"><b>OUR</b> APPROACH</h2>
  <div style="position:absolute;left:0;right:0;top:58px;text-align:center;font-size:6.6px;line-height:8px;color:#222">USE OF FOUNDER SEED CAPITAL<br>$1.12M SINCE JAN 2014</div>
  <div style="position:absolute;left:0;right:0;top:78px;display:flex;justify-content:center;gap:5px;font-size:3.4px;color:#555">
    <span><i style="display:inline-block;width:3px;height:3px;background:#4f8fd6"></i> marketing</span>
    <span><i style="display:inline-block;width:3px;height:3px;background:#f08a2a"></i> sg&amp;a</span>
    <span><i style="display:inline-block;width:3px;height:3px;background:#9b9b9b"></i> r&amp;d</span>
    <span><i style="display:inline-block;width:3px;height:3px;background:#f2c21b"></i> 1x legal</span>
  </div>
  <svg style="position:absolute;left:84px;top:90px" width="100" height="100" viewBox="0 0 100 100" role="img" aria-label="Donut chart: r&amp;d 60%, sg&amp;a 21%, marketing 12%, legal 7%">
    <g transform="rotate(-90 50 50)" fill="none" stroke-width="16">
      <circle cx="50" cy="50" r="38" stroke="#4f8fd6" stroke-dasharray="28.65 238.76"/>
      <circle cx="50" cy="50" r="38" stroke="#f08a2a" stroke-dasharray="50.14 238.76" stroke-dashoffset="-28.65"/>
      <circle cx="50" cy="50" r="38" stroke="#9b9b9b" stroke-dasharray="143.26 238.76" stroke-dashoffset="-78.79"/>
      <circle cx="50" cy="50" r="38" stroke="#f2c21b" stroke-dasharray="16.71 238.76" stroke-dashoffset="-222.05"/>
    </g>
    <g font-family="Open Sans, sans-serif" font-size="5" fill="#fff" text-anchor="middle">
      <text x="60" y="16">marketing</text><text x="60" y="22">12%</text>
      <text x="84" y="50">sg&amp;a</text><text x="84" y="56">21%</text>
      <text x="26" y="82">r&amp;d</text><text x="26" y="88">60%</text>
      <text x="38" y="14">1x legal</text><text x="38" y="20">7%</text>
    </g>
  </svg>
  <div class="para" style="position:absolute;left:24px;right:24px;top:196px">
    <div class="sub" style="margin-top:0">Solution</div>
    <div class="mini">AI automated accounting</div>
    <p>Ledgerly builds automation in stages on top of its current system to reach full automation. It starts by connecting to all sources of accounting data such as bank accounts, credit cards, webshops and document systems. Based on these data it creates bookings and generates financial reports, acting as a trusted advisor over time.</p>
    <div class="mini">Blockchain software license or Token-as-a-License</div>
    <p>It is possible to create tokens on a blockchain that represent software licenses. Holders are free to transfer or sell them using a secondary market built directly on the chain, which checks each token.</p>
  </div>
  <footer class="foot"><div class="url">www.website.com</div><div class="logo sm"><span>CIVITAS</span><span class="dot"></span></div><div class="num">01</div></footer>
</section>

<!-- Thank you -->
<section class="page c4 r3">
  <div style="position:absolute;left:0;right:0;top:245px;text-align:center;font-size:20px;font-weight:700;color:var(--purple)">Thank You</div>
  <div style="position:absolute;left:64px;top:318px;display:flex;align-items:center;gap:5px">
    <div class="logo sm" style="position:static;font-size:8px"><span>CIVITAS</span><span class="dot"></span></div>
    <div style="border-left:.5px solid var(--silver);padding-left:4px;font-size:3.4px;line-height:4.6px;color:#444">Address line 1 Street Name<br>Area Code, City Name</div>
    <div style="border-left:.5px solid var(--silver);padding-left:4px;font-size:3.4px;line-height:4.6px;color:#444">info@example.org<br><span style="color:var(--purple)">www.website.com</span></div>
  </div>
</section>

</body>
</html>
```